Weight Management Brochure

I would like to take the information on our website tarnwellnessplan.org and translate this into a professional brochure.
There is information about our weight management program that is similar to the marketing of the company quivofit.com which can be used as a resource as well. details of our service as outlined on our website tarnwellnessplan.org, facebook and instagram logo, website, address, phone number, logo. health related images

Target Market(s)

18 and older, men and women interested in weight management services

Industry/Entity Type

Nutrition

Requirements
Must have
• SERVICES
• Medically supervised weight management through collaboration with Physician or Nurse Practitioner, and Registered Dietician
• Weight Loss Prescription management
• Body composition scale analysis at every office visit
• Customized determination of ideal weight and personalized caloric/nutrient needs
• Analysis of daily eating patterns, nutritional education, and personalized nutrition planning support
• Medical nutrition therapy for variety of disease states including: diabetes, cardiovascular disease, hypertension, high cholesterol, gastrointestinal disorders, and sleep apnea
• Nutrition counseling for all weight goals (weight loss, maintenance, or gain)
• Individualized menu planning, healthy eating habit education and advice, custom exercise prescription
• Cognitive behavior therapy, motivational interviewing
• Full and Partial meal replacement optionsOPTIONS
• Visit Options
• Medical Consultation and follow ups
• Registered Dietitian Consultation and follow ups
• Daily Health coaching
• Online Virtual Medical, Dietitian or Health Coaching Virtual visits
Nice to have
• Bio's of the providers if room is available
Should not have
• pictures of people (man or woman) unless its non discriminatory

```html
<!DOCTYPE html>
<html lang="en">
<head>
<meta charset="utf-8">
<title>Tarn Wellness – Weight Management Brochure</title>
<link rel="stylesheet" href="https://fonts.googleapis.com/css2?family=Montserrat:wght@400;500;600;800&family=Open+Sans:wght@400;600&family=Roboto+Slab:wght@300;400;700;800&display=swap">
<style>
  :root {
    --navy: #0f1a2e;
    --ink: #1d2b4f;
    --blue: #3f86c9;
    --blue-dark: #1f5a9a;
    --gold: #c9a227;
    --text: #1b1b1b;
    --white: #ffffff;
  }
  * { box-sizing: border-box; margin: 0; padding: 0; }
  html, body { width: 1200px; height: 972px; overflow: hidden; background: #f4f4f4; }
  .brochure { position: relative; width: 1200px; height: 972px; background: var(--white); overflow: hidden; font-family: "Open Sans", Arial, sans-serif; }
  .backdrop { position: absolute; left: 0; top: 0; }

  .faq { position: absolute; left: 31px; width: 340px; }
  .faq h2 { font-family: "Roboto Slab", Georgia, serif; font-weight: 300; font-size: 21px; color: #333; margin-bottom: 10px; white-space: nowrap; }
  .faq h2 strong { font-weight: 700; color: var(--blue); }
  .faq p { font-size: 14px; line-height: 20.5px; color: var(--text); text-align: justify; }

  .welcome { position: absolute; left: 392px; width: 396px; top: 30px; text-align: center; font-family: "Roboto Slab", Georgia, serif; }
  .welcome .lead { font-weight: 300; font-size: 40px; color: var(--ink); line-height: 44px; }
  .welcome .big { font-weight: 700; font-size: 58px; line-height: 58px; color: var(--blue); }

  .brand { position: absolute; display: flex; flex-direction: column; align-items: center; text-align: center; }
  .brand .dot { width: 74px; height: 74px; border-radius: 50%; background: var(--blue); margin-bottom: 12px; }
  .brand .name { font-family: "Montserrat", Arial, sans-serif; font-weight: 800; font-size: 24px; letter-spacing: 1px; }
  .brand-mid { left: 392px; width: 396px; top: 252px; }
  .brand-mid .name { color: var(--ink); }
  .brand-right { left: 787px; width: 413px; top: 610px; }
  .brand-right .dot { width: 96px; height: 96px; }
  .brand-right .name { color: var(--white); font-size: 26px; }

  .team { position: absolute; left: 392px; width: 396px; top: 402px; text-align: center; font-family: "Montserrat", Arial, sans-serif; color: var(--ink); }
  .team li { list-style: none; font-weight: 800; font-size: 21px; line-height: 24px; margin-bottom: 10px; }
  .team li span { display: block; font-weight: 500; font-size: 16px; line-height: 20px; }

  .schedule { position: absolute; left: 392px; width: 400px; top: 730px; text-align: center; font-family: "Montserrat", Arial, sans-serif; color: var(--white); }
  .schedule .kicker { font-weight: 400; font-size: 18px; letter-spacing: .5px; line-height: 22px; }
  .schedule h3 { font-weight: 800; font-size: 25px; color: var(--blue); line-height: 28px; }
  .schedule .rule { width: 50px; height: 2px; background: var(--gold); margin: 8px auto 12px; }
  .schedule .intro { font-size: 13.5px; color: var(--blue); margin-bottom: 4px; }
  .schedule .line { font-size: 13.5px; line-height: 21px; display: flex; justify-content: center; align-items: center; gap: 6px; color: var(--white); }
  .schedule .line svg { width: 13px; height: 13px; flex: none; }
  .schedule .hours-label { margin-top: 9px; font-size: 13px; color: var(--blue); }
  .schedule .hours { font-size: 13px; font-weight: 600; color: var(--white); }

  .cover-title { position: absolute; left: 787px; width: 413px; top: 814px; text-align: center; font-family: "Roboto Slab", Georgia, serif; }
  .cover-title .sub { color: var(--white); font-weight: 400; font-size: 29px; line-height: 32px; }
  .cover-title .main { color: var(--blue); font-weight: 800; font-size: 48px; line-height: 52px; }
  .cover-title .rule { width: 54px; height: 2px; background: var(--blue-dark); margin: 8px auto 10px; }
  .cover-title .url { font-family: "Montserrat", Arial, sans-serif; color: var(--white); font-size: 15px; letter-spacing: .3px; }
</style>
</head>
<body>
<main class="brochure">
  <svg class="backdrop" width="1200" height="972" viewBox="0 0 1200 972">
    <defs>
      <linearGradient id="fruitTone" x1="0" y1="0" x2="1" y2="1">
        <stop offset="0" stop-color="#f7d24a"/>
        <stop offset=".45" stop-color="#e8542f"/>
        <stop offset="1" stop-color="#7a1d2a"/>
      </linearGradient>
      <linearGradient id="appleTone" x1="0" y1="0" x2="0" y2="1">
        <stop offset="0" stop-color="#ffffff"/>
        <stop offset=".45" stop-color="#c8302b"/>
        <stop offset="1" stop-color="#8e1616"/>
      </linearGradient>
      <linearGradient id="stripTone" x1="0" y1="0" x2="0" y2="1">
        <stop offset="0" stop-color="#ffffff"/>
        <stop offset="1" stop-color="#d9dcdf"/>
      </linearGradient>
      <linearGradient id="panelShade" x1="0" y1="0" x2="1" y2="0">
        <stop offset="0" stop-color="#e9ebee"/>
        <stop offset=".5" stop-color="#ffffff"/>
        <stop offset="1" stop-color="#eef0f2"/>
      </linearGradient>
      <clipPath id="rightPanels"><rect x="392" y="0" width="808" height="972"/></clipPath>
      <clipPath id="leftPanel"><rect x="0" y="0" width="392" height="972"/></clipPath>
    </defs>

    <rect x="392" y="0" width="396" height="972" fill="url(#panelShade)"/>
    <rect x="160" y="560" width="400" height="200" fill="url(#stripTone)" role="img" aria-label="Faded photo strip of a sandwich, a tape measure and green apples"/>
    <rect x="787" y="0" width="413" height="560" fill="url(#fruitTone)" role="img" aria-label="Photo of colourful sliced fruit: oranges, grapefruit, berries, kiwi and pineapple"/>

    <g clip-path="url(#rightPanels)">
      <path d="M0,596 C150,720 300,745 420,725 C600,690 700,575 850,548 C1000,522 1120,515 1200,525 L1200,972 L0,972 Z" fill="var(--navy)"/>
    </g>
    <g clip-path="url(#leftPanel)">
      <path d="M0,596 C150,720 300,745 420,725 C600,690 700,575 850,548 C1000,522 1120,515 1200,525 L1200,972 L0,972 Z" fill="var(--white)"/>
    </g>

    <path d="M0,606 C150,730 300,755 420,735 C600,700 700,585 850,558 C1000,532 1120,525 1200,535" fill="none" stroke="#c9d3de" stroke-width="3"/>
    <path d="M0,596 C150,720 300,745 420,725 C600,690 700,575 850,548 C1000,522 1120,515 1200,525" fill="none" stroke="var(--blue-dark)" stroke-width="11"/>

    <rect x="0" y="762" width="392" height="210" fill="url(#appleTone)" role="img" aria-label="Photo of red apples, one wrapped in a tape measure"/>
  </svg>

  <section class="faq" style="top:42px">
    <h2>What exactly is <strong>“ The Program ” ?</strong></h2>
    <p>We are founded on the understanding that no two people are the same, so no two plans are the same. There is no “program”, each patient’s plan is based on their health status and goals while keeping lifestyle and preferences in consideration.</p>
  </section>
  <section class="faq" style="top:234px">
    <h2>Do I <strong>Have to take Medication ?</strong></h2>
    <p>Medication is not required, although it may be a helpful option that we are able to offer for some patients. The healthcare provider will sit down with you to review your information and make recommendations that are suitable for you – both with and without medication.</p>
  </section>
  <section class="faq" style="top:418px">
    <h2>Will My <strong>Insurance Cover My Visits ?</strong></h2>
    <p>Prior to your visit you’ll speak to one of our qualified billing experts, who will check your plan’s coverage and go over the details with you so there are no surprises after you meet with us. We also have non-insurance payment options available.</p>
  </section>

  <header class="welcome">
    <div class="lead">Welcome to a</div>
    <div class="big">Healthier<br>You!</div>
  </header>

  <div class="brand brand-mid">
    <div class="dot"></div>
    <div class="name">TARN WELLNESS</div>
  </div>

  <ul class="team">
    <li>Dr. Owen Halvers</li>
    <li>Mara Ellwood, NP-BC</li>
    <li>Priya Castellan,<span>MS RDN CDN CDE CSCS</span></li>
    <li>Tessa Brookline, RDN</li>
  </ul>

  <section class="schedule">
    <div class="kicker">HOW DO I SCHEDULE</div>
    <h3>AN APPOINTMENT</h3>
    <div class="rule"></div>
    <p class="intro">Our staff will gladly schedule you for an appointment:</p>
    <p class="line"><svg viewBox="0 0 12 12"><path d="M6 0.5a4 4 0 0 0-4 4c0 3 4 7 4 7s4-4 4-7a4 4 0 0 0-4-4z" fill="var(--blue)"/><circle cx="6" cy="4.5" r="1.5" fill="var(--navy)"/></svg>1480 Linden Parkway, Suite 210,</p>
    <p class="line">Maple Ridge, NY 11990</p>
    <p class="line"><svg viewBox="0 0 12 12"><circle cx="6" cy="6" r="6" fill="var(--blue)"/><path d="M4 3l1.3 1.6-.7.9c.5 1 1.2 1.7 2 2l.8-.7L9 8.1 8.2 9C6 8.7 3.5 6.2 3.2 4z" fill="var(--navy)"/></svg>(555) 014-2200 &nbsp;<svg viewBox="0 0 12 12"><circle cx="6" cy="6" r="6" fill="var(--blue)"/><rect x="3.5" y="5" width="5" height="3" fill="var(--navy)"/><rect x="4.5" y="3" width="3" height="2" fill="var(--navy)"/></svg>(555) 014-2201</p>
    <p class="line"><svg viewBox="0 0 12 12"><circle cx="6" cy="6" r="5.2" fill="none" stroke="var(--blue)" stroke-width="1.3"/><path d="M1 6h10M6 1c-2 3-2 7 0 10M6 1c2 3 2 7 0 10" stroke="var(--blue)" stroke-width="1" fill="none"/></svg>www.tarnwellnessplan.org</p>
    <p class="hours-label">Administrative Office Hours:</p>
    <p class="hours">Monday 10am-8pm, Tuesday-Friday 9am-5pm</p>
  </section>

  <div class="brand brand-right">
    <div class="dot"></div>
    <div class="name">TARN WELLNESS</div>
  </div>

  <section class="cover-title">
    <div class="sub">WEIGHT MANAGEMENT</div>
    <div class="main">SERVICES</div>
    <div class="rule"></div>
    <div class="url">www.tarnwellnessplan.org</div>
  </section>
</main>
</body>
</html>
```